We need a refreshed business card. Our company is a venture capital investment firm focused on investing in medical devices. Logo is attached. please also see our website www.velmoracapital.example

Target Market(s)

investors and potential investment targets

Industry/Entity Type

medical investments

Contact Information for Business Card

logo, name, title, email, phone, website, address,

Colors
0054AA
0677BA
7BADD7
CADEEF
E8F1F8
0094D4
00A9DD
6FCCEA
C7EBF8
E9F6FB
00AB8E
00BBA5
67D7C9
C6EFE9
E9F9F6

Requirements
Must have
• fresh modern design
Nice to have
• QR code leading to our linked in page, short description of what we do “Early Stage Medical Device Investors”

```html
<!DOCTYPE html>
<html lang="en">
<head>
<meta charset="utf-8">
<title>Velmora Capital Partners – Business Card</title>
<link href="https://fonts.googleapis.com/css2?family=Open+Sans:wght@400;600&family=Roboto+Condensed:wght@400&display=swap" rel="stylesheet">
<style>
  :root {
    --page-bg: #e6e7e8;
    --card-bg: #ffffff;
    --brand-blue: #0d56a3;
    --brand-teal: #12b197;
    --ink-navy: #1d3a6e;
    --ink-grey: #3c3c3c;
    --icon-blue: #1e9ad6;
    --rule: #5a6b86;
  }
  * { margin: 0; padding: 0; box-sizing: border-box; }
  html, body { width: 1200px; height: 1200px; overflow: hidden; }
  body {
    background: var(--page-bg);
    font-family: "Open Sans", Arial, sans-serif;
    position: relative;
  }
  .card {
    position: absolute;
    left: 213px;
    width: 774px;
    height: 442px;
    background: var(--card-bg);
    overflow: hidden;
  }
  .card--front { top: 123px; }
  .card--back { top: 634px; }
  .card__wave { position: absolute; left: 0; top: 0; width: 774px; height: 442px; }

  /* Front */
  .front-brand {
    position: absolute;
    left: 33px;
    top: 160px;
    font-size: 44px;
    font-weight: 600;
    color: var(--brand-blue);
    line-height: 1;
  }
  .front-brand__rule {
    position: absolute;
    left: 204px;
    top: 145px;
    width: 1px;
    height: 88px;
    background: var(--rule);
  }
  .front-brand__name {
    position: absolute;
    left: 220px;
    top: 164px;
    font-size: 14px;
    letter-spacing: 1.6px;
    line-height: 17.5px;
    color: var(--ink-grey);
    text-transform: uppercase;
  }
  .front-divider {
    position: absolute;
    left: 374px;
    top: 100px;
    width: 3px;
    height: 180px;
    background: linear-gradient(to bottom, rgba(0,0,0,0), rgba(0,0,0,0.12) 50%, rgba(0,0,0,0));
  }
  .contact-list {
    position: absolute;
    left: 398px;
    top: 129px;
    list-style: none;
  }
  .contact-list__item {
    display: flex;
    align-items: center;
    height: 31.6px;
    font-size: 20px;
    letter-spacing: 0.6px;
    color: var(--ink-navy);
  }
  .contact-list__icon { width: 20px; height: 20px; margin-right: 9px; flex: none; }

  /* Back */
  .back-brand {
    position: absolute;
    left: 0;
    width: 100%;
    top: 112px;
    text-align: center;
    font-size: 92px;
    font-weight: 600;
    color: var(--brand-blue);
    line-height: 1;
  }
  .back-name {
    position: absolute;
    left: 0;
    width: 100%;
    top: 249px;
    text-align: center;
    font-family: "Roboto Condensed", "Arial Narrow", sans-serif;
    font-size: 23px;
    color: var(--ink-grey);
    text-transform: uppercase;
  }
</style>
</head>
<body>

<section class="card card--front">
  <svg class="card__wave" viewBox="0 0 774 442" aria-hidden="true">
    <path fill="var(--brand-teal)" d="M0,372 C60,325 180,318 300,348 C420,378 540,418 640,408 C700,402 740,380 774,348 L774,442 L0,442 Z"/>
    <path fill="var(--brand-blue)" d="M0,378 C70,336 190,334 310,362 C430,390 550,420 650,414 C705,410 745,386 774,352 L774,442 L0,442 Z"/>
  </svg>

  <div class="front-brand">Velmora</div>
  <div class="front-brand__rule"></div>
  <div class="front-brand__name">Velmora<br>Capital<br>Partners</div>

  <div class="front-divider"></div>

  <ul class="contact-list">
    <li class="contact-list__item">
      <svg class="contact-list__icon" viewBox="0 0 20 20" aria-hidden="true">
        <circle cx="10" cy="10" r="8.5" fill="none" stroke="var(--icon-blue)" stroke-width="2"/>
        <path fill="var(--icon-blue)" d="M7 5.5l1.6 0 .8 2.4-1.1.9c.6 1.3 1.5 2.2 2.8 2.8l.9-1.1 2.4.8 0 1.6c0 .6-.5 1-1.1 1-3.8-.3-6.7-3.2-7.1-7 0-.8.4-1.4.8-1.4z"/>
      </svg>
      +1 555 0142 860
    </li>
    <li class="contact-list__item">
      <svg class="contact-list__icon" viewBox="0 0 20 20" aria-hidden="true">
        <rect x="1" y="4" width="18" height="12" fill="var(--icon-blue)"/>
        <path d="M1.5 4.5 L10 11 L18.5 4.5" fill="none" stroke="#fff" stroke-width="1.4"/>
      </svg>
      hello@velmoracapital.example
    </li>
    <li class="contact-list__item">
      <svg class="contact-list__icon" viewBox="0 0 20 20" aria-hidden="true">
        <path fill="var(--icon-blue)" d="M10 1a7 7 0 0 0-7 7c0 5 7 11 7 11s7-6 7-11a7 7 0 0 0-7-7z"/>
        <circle cx="10" cy="8" r="3" fill="#fff"/>
      </svg>
      48 Harbor Lane, Suite 210
    </li>
    <li class="contact-list__item">
      <svg class="contact-list__icon" viewBox="0 0 20 20" aria-hidden="true">
        <circle cx="10" cy="10" r="9" fill="var(--icon-blue)"/>
        <path d="M4 7c2 0 3 1 3 3s2 2 2 4M12 3c0 2 2 3 4 3M12 17c0-2 1-3 3-3" fill="none" stroke="#fff" stroke-width="1.5"/>
      </svg>
      www.velmoracapital.example
    </li>
  </ul>
</section>

<section class="card card--back">
  <svg class="card__wave" viewBox="0 0 774 442" aria-hidden="true">
    <path fill="var(--brand-blue)" d="M0,372 C60,325 180,318 300,348 C420,378 540,418 640,408 C700,402 740,380 774,348 L774,442 L0,442 Z"/>
    <path fill="var(--brand-teal)" d="M0,378 C70,336 190,334 310,362 C430,390 550,420 650,414 C705,410 745,386 774,352 L774,442 L0,442 Z"/>
  </svg>

  <div class="back-brand">Velmora</div>
  <div class="back-name">Velmora Capital Partners</div>
</section>

</body>
</html>
```